Monthly Wall Calendar for German shepherd Rescue

We will provide photo's description of dogs and placement of photos and all written material for calendar. We need a wall calendar and we will need as a final output pdf files with the proper bleed lines to send to printer. We have uploaded what the prior year calendar looked like. We are looking for something similar this year.

Generally there is a large monthly photo and 2-3 smaller ones added to the calendar page.

Target Market(s)

Our supporters and animal rescue people.

Font styles to use
Serif

Colors
6c459b
b7a5cd

Requirements
Must have
• A final pdf file with bleed lines for printer.
Nice to have
• The uploaded calendar gives a nice idea of what we are looking for as well as this link. http://brimleyhaven.com/calendar-2016-photo-spread/ and http://brimleyhaven.com/covers-2017/
Should not have
• Not cluttered

```html
<!DOCTYPE html>
<html lang="en">
<head>
<meta charset="utf-8">
<title>Brimley Haven Rescue – 2018 Wall Calendar</title>
<link rel="stylesheet" href="https://fonts.googleapis.com/css2?family=Exo+2:wght@400;500&family=Quicksand:wght@400;500;600&display=swap">
<style>
:root{
  --bg:#eeedf1;
  --paper:#ffffff;
  --brand:#6c459b;
  --lavender:#b7a5cd;
  --ink-purple:#4b3a6e;
  --accent:#3b9fc6;
  --weekend:#c4e1eb;
  --weekday:#ececec;
  --grey-text:#8a8a8a;
  --day-text:#555555;
  --frame:#9fd0e3;
  --tile-blue:#bcd8ec;
  --tile-pink:#d9ab9c;
  --tile-brown:#7a5331;
}
*{box-sizing:border-box;margin:0;padding:0}
html,body{width:1200px;height:1000px;overflow:hidden}
body{background:var(--bg);font-family:"Quicksand",sans-serif;position:relative}

.page{position:absolute;top:220px;width:360px;height:560px;background:var(--paper);box-shadow:0 4px 14px rgba(60,50,80,.18);overflow:hidden}
.page--cover{left:30px}
.page--january{left:420px}
.page--august{left:810px}

/* cover */
.cover-frame{position:absolute;inset:14px;border:1px solid var(--frame)}
.cover-frame--inner{inset:20px;border-color:#d6d6de}
.tile{position:absolute;width:70px;height:70px}
.tile--blue{background:var(--tile-blue)}
.tile--pink{background:var(--tile-pink)}
.tile--brown{background:var(--tile-brown)}
.greeting{position:absolute;left:30px;top:298px;width:80px;text-align:right;font-family:"Exo 2",sans-serif;font-size:15px;line-height:1.15;color:var(--ink-purple)}
.cover-year{position:absolute;left:112px;top:318px;font-family:"Exo 2",sans-serif;font-weight:400;font-size:58px;line-height:1;letter-spacing:1px;color:var(--ink-purple)}
.brand{display:flex;align-items:center;gap:6px;color:var(--brand);font-family:"Quicksand",sans-serif;font-weight:600}
.brand__dot{width:10px;height:10px;border-radius:50%;background:var(--lavender);flex:none}
.cover-brand{position:absolute;left:0;right:0;top:428px;justify-content:center;font-size:19px}
.contact-bone{position:absolute;left:92px;top:470px;width:176px;height:42px;border-radius:21px;background:#9d8bb8;color:#fff;font-size:6px;font-style:normal;line-height:1.35;text-align:center;padding-top:9px}

/* month page */
.month-art{position:absolute;left:0;top:0}
.month-head{position:absolute;left:16px;top:296px;display:flex;align-items:center;font-family:"Exo 2",sans-serif}
.month-head__num{font-size:40px;font-weight:500;color:var(--accent);padding-right:8px;border-right:1px solid #bbb;line-height:1}
.month-head__text{padding-left:7px;line-height:1}
.month-head__name{font-size:25px;color:var(--accent)}
.month-head__year{font-size:15px;color:var(--grey-text);letter-spacing:1px}
.note-lines{position:absolute;left:166px;top:304px;width:72px}
.note-lines span{display:block;height:7px;border-bottom:1px solid #d8d8d8}

.month-grid{position:absolute;left:14px;top:352px;width:228px;display:grid;grid-template-columns:repeat(7,1fr);gap:2px}
.month-grid__dow{font-size:5.5px;color:var(--grey-text);text-align:center;height:12px;font-weight:600}
.month-grid__dow--weekend{color:var(--accent)}
.day{height:32px;background:var(--weekday);font-size:10px;color:var(--day-text);text-align:center;padding-top:5px;font-family:"Exo 2",sans-serif}
.day--weekend{background:var(--weekend);color:#2a86ad}
.day--empty{color:transparent}

.side-brand{position:absolute;left:252px;top:400px;font-size:10px;width:100px;line-height:1.1}
.mini-cal{position:absolute;left:252px;top:432px;width:96px}
.mini-cal__title{font-size:6px;color:var(--accent);text-align:center;letter-spacing:.5px;margin-bottom:4px;font-weight:600}
.mini-cal__grid{display:grid;grid-template-columns:repeat(7,1fr);row-gap:2px;font-size:6px;color:#555;text-align:center}
.mini-cal__grid .we{color:var(--accent)}
.photo-label{font-family:"Quicksand",sans-serif}
</style>
</head>
<body>

<!-- Cover -->
<section class="page page--cover" aria-label="Calendar cover 2018">
  <div class="cover-frame"></div>
  <div class="cover-frame cover-frame--inner"></div>

  <svg class="tile" style="left:116px;top:80px" viewBox="0 0 70 70" role="img" aria-label="Photo: shepherd dog in snow by a building">
    <defs><linearGradient id="gSnow" x1="0" y1="0" x2="0" y2="1"><stop offset="0" stop-color="#7fa9d6"/><stop offset=".5" stop-color="#8a6a52"/><stop offset="1" stop-color="#e9eef3"/></linearGradient></defs>
    <rect width="70" height="70" fill="url(#gSnow)"/>
  </svg>
  <div class="tile tile--blue" style="left:192px;top:72px"></div>
  <svg class="tile" style="left:40px;top:156px;height:60px" viewBox="0 0 70 60" role="img" aria-label="Photo: shepherd dog running on grass">
    <defs><linearGradient id="gRun" x1="0" y1="0" x2="0" y2="1"><stop offset="0" stop-color="#7d7060"/><stop offset="1" stop-color="#9aa65d"/></linearGradient></defs>
    <rect width="70" height="60" fill="url(#gRun)"/>
  </svg>
  <div class="tile tile--pink" style="left:116px;top:156px"></div>
  <svg class="tile" style="left:192px;top:156px" viewBox="0 0 70 70" role="img" aria-label="Photo: two shepherd dogs on a deck">
    <defs><linearGradient id="gDeck" x1="0" y1="0" x2="0" y2="1"><stop offset="0" stop-color="#6f8d4e"/><stop offset="1" stop-color="#a48b6c"/></linearGradient></defs>
    <rect width="70" height="70" fill="url(#gDeck)"/>
  </svg>
  <div class="tile tile--blue" style="left:268px;top:148px"></div>
  <div class="tile tile--brown" style="left:116px;top:232px"></div>
  <svg class="tile" style="left:192px;top:232px" viewBox="0 0 70 70" role="img" aria-label="Photo: shepherd dog with red bandana in a garden">
    <defs><linearGradient id="gGarden" x1="0" y1="0" x2="0" y2="1"><stop offset="0" stop-color="#4f7a3c"/><stop offset="1" stop-color="#7b5a3c"/></linearGradient></defs>
    <rect width="70" height="70" fill="url(#gGarden)"/>
  </svg>
  <svg class="tile" style="left:268px;top:224px" viewBox="0 0 70 70" role="img" aria-label="Photo: shepherd dog lying on a lawn">
    <defs><linearGradient id="gLawn" x1="0" y1="0" x2="0" y2="1"><stop offset="0" stop-color="#7f9a5a"/><stop offset="1" stop-color="#5f8a34"/></linearGradient></defs>
    <rect width="70" height="70" fill="url(#gLawn)"/>
  </svg>
  <svg class="tile" style="left:268px;top:300px" viewBox="0 0 70 70" role="img" aria-label="Photo: shepherd dog resting outdoors">
    <defs><linearGradient id="gRest" x1="0" y1="0" x2="0" y2="1"><stop offset="0" stop-color="#8b7b62"/><stop offset="1" stop-color="#6a7d45"/></linearGradient></defs>
    <rect width="70" height="70" fill="url(#gRest)"/>
  </svg>

  <p class="greeting">Happy<br>New Year</p>
  <h1 class="cover-year">2018</h1>
  <div class="brand cover-brand"><span class="brand__dot"></span>Brimley Haven Rescue</div>
  <address class="contact-bone">PO Box 210, Hollis Bay, NJ 07000<br>Phone: 555.014.2290 • email: hello@brimleyhaven.com<br>brimleyhaven.com</address>
</section>

<!-- January -->
<section class="page page--january" aria-label="January 2018">
  <svg class="month-art" width="360" height="400" viewBox="0 0 360 400">
    <defs>
      <linearGradient id="gJanMain" x1="0" y1="0" x2="0" y2="1"><stop offset="0" stop-color="#3f5a2c"/><stop offset=".45" stop-color="#6d5a3f"/><stop offset="1" stop-color="#6f9a42"/></linearGradient>
      <linearGradient id="gJanA" x1="0" y1="0" x2="1" y2="1"><stop offset="0" stop-color="#8a7b6b"/><stop offset="1" stop-color="#3a3028"/></linearGradient>
      <linearGradient id="gJanB" x1="0" y1="0" x2="1" y2="1"><stop offset="0" stop-color="#b0733e"/><stop offset="1" stop-color="#5e3f28"/></linearGradient>
    </defs>
    <polygon points="0,0 360,0 360,240 248,290 0,255" fill="url(#gJanMain)" role="img" aria-label="Photo: Biscuit, a German shepherd lying on grass"/>
    <polygon points="252,296 360,248 360,320" fill="url(#gJanA)" role="img" aria-label="Photo: close-up of a shepherd dog"/>
    <polygon points="248,306 360,328 360,362 248,388" fill="url(#gJanB)" role="img" aria-label="Photo: shepherd dog indoors"/>
    <rect x="205" y="212" width="155" height="26" fill="#fff" opacity=".55"/>
    <rect x="218" y="219" width="12" height="12" fill="var(--lavender)"/>
    <text class="photo-label" x="250" y="231" font-size="14" font-weight="600" fill="var(--accent)">Biscuit</text>
    <rect x="316" y="306" width="34" height="9" fill="#fff" opacity=".6"/>
    <text class="photo-label" x="333" y="312.5" font-size="5.5" text-anchor="middle" fill="#555">Rook</text>
    <rect x="254" y="372" width="30" height="9" fill="#fff" opacity=".6"/>
    <text class="photo-label" x="269" y="378.5" font-size="5.5" text-anchor="middle" fill="#555">Tansy</text>
  </svg>

  <div class="month-head">
    <span class="month-head__num">1</span>
    <div class="month-head__text"><div class="month-head__name">January</div><div class="month-head__year">2018</div></div>
  </div>
  <div class="note-lines"><span></span><span></span><span></span><span></span></div>

  <div class="month-grid">
    <div class="month-grid__dow">SUN</div><div class="month-grid__dow">MON</div><div class="month-grid__dow">TUE</div><div class="month-grid__dow">WED</div><div class="month-grid__dow">THU</div><div class="month-grid__dow">FRI</div><div class="month-grid__dow month-grid__dow--weekend">SAT</div>
    <div class="day day--weekend day--empty">0</div><div class="day">1</div><div class="day">2</div><div class="day">3</div><div class="day">4</div><div class="day">5</div><div class="day day--weekend">6</div>
    <div class="day day--weekend">7</div><div class="day">8</div><div class="day">9</div><div class="day">10</div><div class="day">11</div><div class="day">12</div><div class="day day--weekend">13</div>
    <div class="day day--weekend">14</div><div class="day">15</div><div class="day">16</div><div class="day">17</div><div class="day">18</div><div class="day">19</div><div class="day day--weekend">20</div>
    <div class="day day--weekend">21</div><div class="day">22</div><div class="day">23</div><div class="day">24</div><div class="day">25</div><div class="day">26</div><div class="day day--weekend">27</div>
    <div class="day day--weekend">28</div><div class="day">29</div><div class="day">30</div><div class="day">31</div><div class="day day--empty">0</div><div class="day day--empty">0</div><div class="day day--weekend day--empty">0</div>
  </div>

  <div class="brand side-brand"><span class="brand__dot"></span>Brimley Haven Rescue</div>
  <div class="mini-cal">
    <div class="mini-cal__title">FEBRUARY 2018</div>
    <div class="mini-cal__grid">
      <span>S</span><span>M</span><span>T</span><span>W</span><span>T</span><span>F</span><span>S</span>
      <span></span><span></span><span></span><span></span><span>1</span><span>2</span><span class="we">3</span>
      <span class="we">4</span><span>5</span><span>6</span><span>7</span><span>8</span><span>9</span><span class="we">10</span>
      <span class="we">11</span><span>12</span><span>13</span><span>14</span><span>15</span><span>16</span><span class="we">17</span>
      <span class="we">18</span><span>19</span><span>20</span><span>21</span><span>22</span><span>23</span><span class="we">24</span>
      <span class="we">25</span><span>26</span><span>27</span><span>28</span><span></span><span></span><span></span>
    </div>
  </div>
</section>

<!-- August -->
<section class="page page--august" aria-label="August 2018">
  <svg class="month-art" width="360" height="400" viewBox="0 0 360 400">
    <defs>
      <linearGradient id="gAugMain" x1="0" y1="0" x2="0" y2="1"><stop offset="0" stop-color="#5f8a3a"/><stop offset=".5" stop-color="#8a6a4c"/><stop offset="1" stop-color="#a99a86"/></linearGradient>
      <linearGradient id="gAugA" x1="0" y1="0" x2="1" y2="1"><stop offset="0" stop-color="#8a7b6b"/><stop offset="1" stop-color="#3a3028"/></linearGradient>
      <linearGradient id="gAugB" x1="0" y1="0" x2="1" y2="1"><stop offset="0" stop-color="#b0733e"/><stop offset="1" stop-color="#5e3f28"/></linearGradient>
    </defs>
    <polygon points="0,0 360,0 360,240 248,290 0,255" fill="url(#gAugMain)" role="img" aria-label="Photo: Juniper, a German shepherd sitting on a wooden deck"/>
    <polygon points="252,296 360,248 360,320" fill="url(#gAugA)" role="img" aria-label="Photo: close-up of a shepherd dog"/>
    <polygon points="248,306 360,328 360,362 248,388" fill="url(#gAugB)" role="img" aria-label="Photo: shepherd dog indoors"/>
    <rect x="0" y="196" width="150" height="26" fill="#fff" opacity=".55"/>
    <rect x="12" y="203" width="12" height="12" fill="var(--lavender)"/>
    <text class="photo-label" x="36" y="215" font-size="14" font-weight="600" fill="var(--accent)">Juniper</text>
    <rect x="316" y="306" width="34" height="9" fill="#fff" opacity=".6"/>
    <text class="photo-label" x="333" y="312.5" font-size="5.5" text-anchor="middle" fill="#555">Rook</text>
    <rect x="254" y="372" width="30" height="9" fill="#fff" opacity=".6"/>
    <text class="photo-label" x="269" y="378.5" font-size="5.5" text-anchor="middle" fill="#555">Tansy</text>
  </svg>

  <div class="month-head">
    <span class="month-head__num">8</span>
    <div class="month-head__text"><div class="month-head__name">August</div><div class="month-head__year">2018</div></div>
  </div>
  <div class="note-lines"><span></span><span></span><span></span><span></span></div>

  <div class="month-grid">
    <div class="month-grid__dow">SUN</div><div class="month-grid__dow">MON</div><div class="month-grid__dow">TUE</div><div class="month-grid__dow">WED</div><div class="month-grid__dow">THU</div><div class="month-grid__dow">FRI</div><div class="month-grid__dow month-grid__dow--weekend">SAT</div>
    <div class="day day--weekend day--empty">0</div><div class="day day--empty">0</div><div class="day day--empty">0</div><div class="day">1</div><div class="day">2</div><div class="day">3</div><div class="day day--weekend">4</div>
    <div class="day day--weekend">5</div><div class="day">6</div><div class="day">7</div><div class="day">8</div><div class="day">9</div><div class="day">10</div><div class="day day--weekend">11</div>
    <div class="day day--weekend">12</div><div class="day">13</div><div class="day">14</div><div class="day">15</div><div class="day">16</div><div class="day">17</div><div class="day day--weekend">18</div>
    <div class="day day--weekend">19</div><div class="day">20</div><div class="day">21</div><div class="day">22</div><div class="day">23</div><div class="day">24</div><div class="day day--weekend">25</div>
    <div class="day day--weekend">26</div><div class="day">27</div><div class="day">28</div><div class="day">29</div><div class="day">30</div><div class="day">31</div><div class="day day--weekend day--empty">0</div>
  </div>

  <div class="brand side-brand"><span class="brand__dot"></span>Brimley Haven Rescue</div>
  <div class="mini-cal">
    <div class="mini-cal__title">SEPTEMBER 2018</div>
    <div class="mini-cal__grid">
      <span>S</span><span>M</span><span>T</span><span>W</span><span>T</span><span>F</span><span>S</span>
      <span></span><span></span><span></span><span></span><span></span><span></span><span class="we">1</span>
      <span class="we">2</span><span>3</span><span>4</span><span>5</span><span>6</span><span>7</span><span class="we">8</span>
      <span class="we">9</span><span>10</span><span>11</span><span>12</span><span>13</span><span>14</span><span class="we">15</span>
      <span class="we">16</span><span>17</span><span>18</span><span>19</span><span>20</span><span>21</span><span class="we">22</span>
      <span class="we">23</span><span>24</span><span>25</span><span>26</span><span>27</span><span>28</span><span class="we">29</span>
      <span class="we">30</span><span></span><span></span><span></span><span></span><span></span><span></span>
    </div>
  </div>
</section>

</body>
</html>
```